Company brochure for our unique consulting business

We are a small consulting business offering a unique set of services to our clients.. In simple terms we are a business improvement consultancy helping our clients get the best out of their businesses. We work with clients across multiple sectors and deliver a variety of services. We want to put together a brochure to cover these main themes:1. Who we are2. What we do3. The type of people we employ4. The sectors we work inWhile the brochure needs to have a certain corporate feel to it, we don't want it to be "boring" or "stiff". We would like it to have a slightly "friendly" or "informal" feel to it, to reflect the type of organisation we are.We have a company website http://halvorkeyadvisory.example , however we do not want to directly replicate the content or feel as we recognise it needs updating.We would like the brochure to be A4 portrait format. We anticipate requiring 12 sides (including covers) but we are happy to be guided on this based on the content we have provided.The attached ppt file gives the detail of the content to be included and also shows the proposed pagination. For the front cover we would like to try 2 versions, one with the HKA logo and one with the Halvor Key Advisory logo (a file of both is attached)One of the most important pages will be the "Our Services" page. We would like this to cover the centre fold. In the ppt file we have shown an example layout, but this is where we need most help - we are clearly not graphic designers! This page will be the most used page in sales meetings etc.Also attached is the following:1. file for our HalvorKey Advisory company logo.2. File for our HKA company logo3. Files for Oren's signatures (for under photos) - Duncan's to follow4. Photo of Oren & Duncan (person in purple shirt to be cropped out)Thank you and really excited to see what everyone comes back with.Oren & Duncan

Target Market(s)

Very broad - Manufacturing, Healthcare, Hospitality

Industry/Entity Type

Management Consulting

Font styles to use
Other font styles liked:
• We use Swiss721, but happy to be guided by designer

Colors
3276b5
85abd2
0355a3
333333
5c5c5c
9d9d9d
d9d9d9

Requirements
Must have
• Corporate feel
Nice to have
• Slightly friendly feel
• Our standard "blue" is (CORRECTION) - R55 G96 B146 #376092 and our standard grey is R197 G178, B179 - #B3B2B2, which we would like to keep, but other colours we are happy to be guided on. Brand guidelines attached.

```html
<!DOCTYPE html>
<html lang="en">
<head>
<meta charset="utf-8">
<title>Halvor Key Advisory – Values and Regions Spread</title>
<link href="https://fonts.googleapis.com/css2?family=Didact+Gothic&family=Roboto:wght@400;700&display=swap" rel="stylesheet">
<style>
  :root {
    --brand-blue: #3276b5;
    --soft-blue: #85abd2;
    --deep-blue: #0355a3;
    --ink: #333333;
    --ink-mid: #5c5c5c;
    --ink-light: #9d9d9d;
    --rule: #d9d9d9;
    --paper: #ffffff;
    --backdrop: #e6e7ea;
  }
  * { box-sizing: border-box; margin: 0; padding: 0; }
  html, body {
    width: 1200px; height: 900px; overflow: hidden;
    background: var(--backdrop);
  }
  .spread {
    position: absolute; left: 63px; top: 70px;
    width: 1074px; height: 760px;
    display: flex;
    box-shadow: 0 10px 30px rgba(0,0,0,0.12);
  }
  .page {
    position: relative; width: 537px; height: 760px;
    background: var(--paper); overflow: hidden;
  }
  .page--left::after {
    content: ""; position: absolute; top: 0; right: 0; width: 40px; height: 100%;
    background: linear-gradient(to right, rgba(0,0,0,0), rgba(0,0,0,0.08));
  }
  .page--right::after {
    content: ""; position: absolute; top: 0; left: 0; width: 30px; height: 100%;
    background: linear-gradient(to left, rgba(0,0,0,0), rgba(0,0,0,0.07));
  }
  .page-shapes { position: absolute; inset: 0; }

  .section-title {
    font-family: "Didact Gothic", sans-serif;
    font-weight: 400; color: var(--brand-blue);
    letter-spacing: 0.5px;
  }
  .values-title { position: absolute; left: 112px; top: 150px; font-size: 31px; }
  .values-list {
    position: absolute; left: 112px; top: 205px; width: 215px;
    list-style: none;
    font-family: "Didact Gothic", sans-serif;
    font-size: 10.5px; line-height: 1.45; color: var(--ink-mid);
  }
  .values-list li { margin-bottom: 11px; }
  .values-list strong { font-weight: 400; color: var(--ink); }

  .team-photo {
    position: absolute; left: 0; top: 0; width: 537px; height: 365px;
    background: linear-gradient(160deg, #f2f2f2 0%, #d4d4d4 45%, #bdbdbd 75%, #e8e8e8 100%);
  }
  .brand-tile {
    position: absolute; left: 318px; top: 205px; width: 150px; height: 135px;
    background: rgba(133,171,210,0.72);
    transform: rotate(-6deg);
  }
  .brand-name {
    position: absolute; right: 12px; bottom: 36px;
    font-family: "Didact Gothic", sans-serif; font-size: 15px;
    color: var(--ink); line-height: 1;
    transform: rotate(6deg);
  }

  .regions-title { position: absolute; left: 310px; top: 380px; font-size: 23px; }
  .regions-map {
    position: absolute; left: 282px; top: 418px; width: 230px; height: 120px;
    background: radial-gradient(ellipse at 50% 55%, #8a8a8a 0%, #b6b6b6 55%, rgba(255,255,255,0) 75%);
  }

  .partner { position: absolute; left: 92px; font-family: "Roboto", sans-serif; }
  .partner--duncan { top: 410px; }
  .partner--oren { top: 515px; }
  .partner-name { font-size: 10px; font-weight: 700; color: var(--ink); }
  .partner-role, .partner-caption {
    font-size: 8.5px; color: var(--ink-light); margin-left: 40px; line-height: 1.3;
  }
  .partner-signature {
    width: 110px; height: 34px; margin-top: 4px;
    background: linear-gradient(90deg, rgba(60,60,60,0.15), rgba(60,60,60,0.05));
  }
</style>
</head>
<body>
  <main class="spread">
    <section class="page page--left" aria-label="Our values">
      <svg class="page-shapes" viewBox="0 0 537 760" width="537" height="760" aria-hidden="true">
        <polygon points="150,0 537,0 537,120 230,60" fill="#f3f3f4"/>
        <polygon points="110,120 300,0 380,0 150,150" fill="#ececee"/>
        <polygon points="0,470 537,330 537,760 250,760" fill="#eeeef0"/>
        <polygon points="120,520 537,460 537,760 330,760" fill="#e4e4e7"/>
        <polygon points="40,160 112,140 112,270 40,300" fill="#85abd2" opacity="0.85"/>
      </svg>
      <h2 class="section-title values-title">Our values</h2>
      <ul class="values-list">
        <li>Be <strong>TRUSTED</strong> by our team and clients, so that our opinions are sought and our recommendations valued.</li>
        <li>Have a light but lasting relationship with our clients, so we are seen as a <strong>PARTNER</strong> and not an outsider.</li>
        <li>Be focused on return-on-investment and consistently strive to deliver <strong>GREAT VALUE</strong>.</li>
        <li><strong>DEVELOP &amp; INVEST</strong> in our own people to continually stay one step ahead.</li>
        <li>Work relentlessly to deliver results for our clients, but ensure we collectively <strong>ENJOY THE JOURNEY</strong>.</li>
        <li>Take <strong>SOCIAL RESPONSIBILITY</strong> seriously by supporting worthwhile organisations.</li>
      </ul>
    </section>

    <section class="page page--right" aria-label="Partners and our regions">
      <div class="team-photo" role="img" aria-label="Black and white photo of the two partners seated at a meeting table"></div>
      <div class="brand-tile">
        <span class="brand-name">halvorkey advisory</span>
      </div>

      <div class="partner partner--duncan">
        <p class="partner-name">Duncan Halvor</p>
        <p class="partner-role">Partner</p>
        <p class="partner-caption">Signature</p>
        <div class="partner-signature" role="img" aria-label="Handwritten signature of Duncan Halvor"></div>
      </div>
      <div class="partner partner--oren">
        <p class="partner-name">Oren Whitlock</p>
        <p class="partner-role">Partner</p>
        <p class="partner-caption">Signature</p>
        <div class="partner-signature" role="img" aria-label="Handwritten signature of Oren Whitlock"></div>
      </div>

      <h2 class="section-title regions-title">Our Regions</h2>
      <div class="regions-map" role="img" aria-label="Dotted world map with the regions served highlighted in blue"></div>
    </section>
  </main>
</body>
</html>
```